Visually Compelling Flyer Design - Harbor Perks

We are a life insurance company looking to create visually compelling flyers that gain attention of potential buyers and simplify the concept. It should be professional, friendly, approachable in nature. Our logo and several rough drafts are included.
We are looking to refine this look and make it ultra professional, clean and easy to follow. A creative brief with brand guidelines is also included.
FLYER 1 — PAY YOURSELF FIRST
EYEBROW TAG
YOUR COMPANY JUST UPGRADED YOUR BENEFITS
HEADLINE
One small decision. A lifetime of protection.
SUBHEADLINE
Permanent life insurance + long-term care coverage, starting at $1 a day.
EYEBROW TAG
CHOOSE YOUR DAILY INVESTMENT
STAT — TIER 1
$1 / day → $20,000 Life Insurance
STAT — TIER 2 (HERO — make this one biggest/most prominent)
$2 / day → $40,000 Life Insurance
★ Most Popular
STAT — TIER 3
$3 / day → $60,000 Life Insurance
CAPTION
Rate locked at enrollment. Benefit never decreases.
EYEBROW TAG
THREE BENEFITS. ONE POLICY.
SUBHEADLINE
Your money works three ways.
CALLOUT — BENEFIT 1
01 | Cash Value Growth
BODY
Averages 6% annually over the last 50 years — guaranteed never to fall below 3%. Better than any savings account. And if you ever need it, you can borrow against it. It's your money.
CALLOUT — BENEFIT 2
02 | Tax-Free Death Benefit
BODY
From day one, your family is protected. The full benefit is paid tax-free to the person you choose — no waiting period, no exceptions. That's your legacy, preserved.
CALLOUT — BENEFIT 3
03 | Long-Term Care Coverage
BODY
70% of Americans will need long-term care. This plan pays 75% of your benefit — upfront and tax-free — to cover those costs while you're still alive. Your retirement savings stay intact. Your family stays protected.
EYEBROW TAG
ALREADY HAVE LIFE INSURANCE THROUGH WORK?
SUBHEADLINE
That's term. It ends when you need it most.
BODY
Term life insurance is designed for temporary needs — protecting your paycheck, your mortgage, your kids while they're home. When you retire, the house is paid off and your children are grown. Term ends because the need ends.
BODY
But one need never ends: your final expenses and the cost of long-term care. This permanent plan stays with you after retirement — when term coverage is gone and getting new coverage is expensive or impossible.
COMPARISON — LEFT COLUMN HEADER
✕ TERM LIFE
COMPARISON — LEFT COLUMN ITEMS
Gets more expensive with age
Ends at retirement
No cash value
Temporary protection only
COMPARISON — RIGHT COLUMN HEADER
✓ THIS PLAN
COMPARISON — RIGHT COLUMN ITEMS
Rate locked forever at enrollment
Stays with you after retirement
Builds real cash value
Permanent protection for life
EYEBROW TAG
WHAT MAKES THIS DIFFERENT
SUBHEADLINE
Built for you. Stays with you.
CALLOUT
✓ Guaranteed Issued
No medical exams. No questions asked. You qualify.
CALLOUT
✓ Group Rate
Because you work here, you get pricing individuals can't access on their own.
CALLOUT
✓ Rate Locked Forever
Your premium never increases. Your benefit never decreases.
CALLOUT
✓ Portable
Change jobs. Retire. Your policy comes with you at the same rate.
CALLOUT
✓ Family Coverage
Protect your spouse and children under the same plan.
SUBHEADLINE
Protect retirement. Preserve dignity. Plan ahead.
CTA
Be on the lookout for your personalized coverage details.
CAPTION
Brokered by Harbor Perks · Underwritten by TrueLedger
FLYER 2 — THE LONG-TERM CARE REALITY
EYEBROW TAG
WHAT MOST PEOPLE DON'T KNOW — BUT SHOULD
HEADLINE
Most Americans are unprepared. You don't have to be.
SUBHEADLINE
The long-term care gap is real — and it affects families like yours.
EYEBROW TAG
THE NUMBERS ARE HARD TO IGNORE
STAT
70%
of Americans age 65 and older will need some form of long-term care during their lifetime.
CAPTION
Source: Pryce & Lomax, Review of Elder Welfare and Civic Planning, 2018
STAT
3–4%
of Americans over 50 own a private long-term care insurance policy. The gap between who needs it and who has it is staggering.
CAPTION
Source: Stroud & Bellamy, QVT Wellness Wire, 2023
STAT
$700 Billion+
Estimated annual U.S. long-term care cost — and it's growing every year.
CAPTION
Source: Delacroix Wynn & Pasternak, Civic Ledger Council, 2020
STAT
$470 Billion
The estimated value of unpaid care provided by family members every year. That's the real cost — measured in time, stress, and financial sacrifice.
CAPTION
Source: Tillman & Osei, Meridian Bureau
STAT
80%
of total long-term care spending goes directly to assist retirees. This isn't a young person's problem. But the time to plan is now.
CAPTION
SUBHEADLINE
Long-term care doesn't just cost money. It costs families.
BODY
When there's no plan in place, the people you love absorb the impact — financially, emotionally, and physically. Retirement savings built over a lifetime can disappear in months. Family members step back from their own lives to provide care. Dignity becomes a daily negotiation.
BODY
This is not inevitable. A small decision today changes the entire outcome.
EYEBROW TAG
THE SOLUTION
HEADLINE
The Pay Yourself First Principle.
BODY
Take the first $1, $2, or $3 you make every day and invest it in a permanent life insurance policy that includes long-term care coverage — underwritten by TrueLedger, offered through your employer at a group rate, and Guaranteed Issued for everyone.
STAT
$1 / day → $20,000 $2 / day → $40,000 $3 / day → $60,000
BODY
The benefit includes three protections in one: a cash value that grows at an average of 6% annually, a tax-free death benefit for your family, and long-term care coverage that pays 75% of your benefit upfront — tax-free — when you need care most.
SUBHEADLINE
Whether you're single, married, with children or without — there is protection in this plan for you.
HEADLINE
CTA
Look for your personalized offer. Coverage details are coming your way.
CAPTION
COPY RULES FOR DESIGNERS
Headlines are one idea only. Never more than two lines.
Stats stand alone. Never buried in a paragraph.
Body copy maxes at 3 sentences per block. If it's longer, cut it.
The $2/day tier is always the hero. Always.
"Guaranteed Issued" appears on both flyers. It's the most important trust signal.
TrueLedger is always attributed. Always.
The tagline is: Protect retirement. Preserve dignity. Plan ahead. — Use it verbatim.
Target Market(s)
Average Americans with a family - adults looking for life insurance
Industry/Entity Type
Life Insurance & Financial Retirement

```html
<!DOCTYPE html>
<html lang="en">
<head>
<meta charset="utf-8">
<title>Harbor Perks — A lifetime of protection</title>
<link href="https://fonts.googleapis.com/css2?family=Montserrat:wght@300;400;500;600;700;800&display=swap" rel="stylesheet">
<style>
  :root {
    --backdrop: #7a7a7a;
    --paper: #ffffff;
    --blue: #0b4ea2;
    --blue-bright: #1169d4;
    --navy: #0c2577;
    --navy-deep: #0a1f66;
    --teal: #1aafbf;
    --teal-soft: #2bc3cf;
    --ink: #1d1d1f;
    --muted: #4a4a52;
    --rule: #3a3a3a;
  }
  * { box-sizing: border-box; margin: 0; padding: 0; }
  html, body { width: 1004px; height: 1200px; overflow: hidden; }
  body { background: var(--backdrop); font-family: "Montserrat", sans-serif; color: var(--ink); position: relative; }

  .sheet {
    position: absolute; left: 106px; top: 88px;
    width: 838px; height: 1082px;
    background: var(--paper);
    transform: scale(0.9463); transform-origin: 0 0;
    overflow: hidden;
    box-shadow: 0 6px 18px rgba(0,0,0,.35);
  }
  .abs { position: absolute; }

  /* brand */
  .brand { left: 63px; top: 38px; display: flex; align-items: center; gap: 10px; }
  .brand-dot { width: 44px; height: 44px; border-radius: 50%; background: var(--teal); }
  .brand-name { font-size: 20px; font-weight: 700; color: var(--navy-deep); letter-spacing: .3px; }

  .eyebrow-lede { left: 61px; top: 88px; font-size: 22px; font-weight: 400; color: var(--teal); }
  .headline { left: 61px; top: 112px; font-size: 40px; line-height: 38px; font-weight: 800; color: var(--blue); letter-spacing: -.3px; }
  .subhead { left: 61px; top: 197px; font-size: 11.5px; line-height: 14px; color: var(--ink); }
  .subhead b { font-weight: 800; }

  .hero-photo {
    left: 362px; top: -120px; width: 560px; height: 348px; border-radius: 50%;
    border-left: 7px solid var(--blue-bright); border-bottom: 7px solid var(--blue-bright);
    background: linear-gradient(135deg, #e9eef2 0%, #cfd8df 45%, #8a7466 70%, #3d4d63 100%);
  }

  /* section headings */
  .section-title { left: 67px; width: 703px; display: flex; align-items: center; gap: 10px; font-size: 16px; font-weight: 700; color: var(--blue); white-space: nowrap; }
  .section-title::before, .section-title::after { content: ""; flex: 1; height: 1px; background: var(--rule); }
  .section-sub { left: 0; width: 838px; text-align: center; font-size: 10.5px; color: var(--ink); }

  /* tiers */
  .tier { top: 270px; width: 210px; height: 92px; background: var(--blue); color: #fff; text-align: center; }
  .tier.hero { background: var(--teal); }
  .tier-price { margin-top: 6px; font-size: 31px; font-weight: 800; }
  .tier-price small { font-size: 13px; font-weight: 600; vertical-align: 6px; margin-left: 4px; }
  .tier-arrow { display: block; margin: -2px auto 0; }
  .tier-amount { font-size: 21px; font-weight: 800; line-height: 22px; }
  .tier-label { font-size: 11px; font-weight: 600; }
  .tier-tag { left: 372px; top: 262px; background: var(--navy); color: #fff; font-size: 9px; font-weight: 600; padding: 1px 5px; }
  .tier-caption { left: 0; width: 838px; top: 370px; text-align: center; font-size: 13.5px; color: var(--ink); }

  /* benefits */
  .benefit { top: 445px; }
  .benefit-head { display: flex; align-items: center; gap: 8px; margin-bottom: 5px; }
  .icon-disc { width: 36px; height: 36px; border-radius: 50%; background: var(--teal); flex: none; display: flex; align-items: center; justify-content: center; }
  .benefit-title { font-size: 15.5px; font-weight: 700; line-height: 15px; color: var(--ink); }
  .benefit-body { font-size: 10.5px; line-height: 13px; color: var(--muted); }
  .col-rule { top: 445px; width: 1px; height: 120px; background: #999; }

  /* term vs plan */
  .work-title { left: 60px; top: 583px; font-size: 15px; font-weight: 700; line-height: 19px; color: var(--blue); }
  .work-lede { left: 60px; top: 621px; font-size: 10.5px; color: var(--ink); }
  .work-body { left: 60px; width: 290px; font-size: 10.5px; line-height: 13px; color: var(--ink); }

  .compare { left: 380px; top: 580px; width: 378px; height: 207px; display: grid; grid-template-columns: 176px 202px; grid-template-rows: 27px 1fr; }
  .compare-head { background: var(--teal); color: #fff; font-size: 15px; font-weight: 700; padding: 4px 0 0 12px; }
  .compare-head + .compare-head { padding-left: 45px; }
  .compare-col { list-style: none; padding: 20px 10px 0 40px; color: #fff; font-size: 10.5px; font-weight: 700; line-height: 13px; }
  .compare-col.term { background: var(--blue-bright); }
  .compare-col.plan { background: var(--blue); padding-left: 45px; }
  .compare-col li { position: relative; margin-bottom: 14px; }
  .compare-col.plan li { margin-bottom: 12px; }
  .compare-col li::before { content: ""; position: absolute; left: -15px; top: 3px; width: 6px; height: 6px; border-radius: 50%; background: var(--teal-soft); }

  /* features */
  .feature { top: 845px; display: flex; gap: 6px; }
  .feature-icon { flex: none; margin-top: 2px; }
  .feature-title { font-size: 13px; font-weight: 700; line-height: 12px; color: var(--blue); }
  .feature-title.teal { color: var(--teal); }
  .feature-body { margin-top: 3px; font-size: 9px; line-height: 11.5px; color: var(--blue); }
  .feature-rule { top: 845px; width: 1px; height: 80px; background: #aaa; }

  /* footer */
  .footer { left: 0; top: 948px; width: 838px; height: 134px; background: var(--navy-deep); color: #fff; }
  .tagline { position: absolute; left: 63px; top: 12px; font-size: 21px; font-weight: 700; line-height: 27px; }
  .tagline .accent { color: var(--teal-soft); }
  .footer-rule { position: absolute; left: 333px; top: 14px; width: 1px; height: 66px; background: rgba(255,255,255,.6); }
  .footer-info { position: absolute; left: 392px; top: 16px; font-size: 12px; font-weight: 700; line-height: 22px; }
  .footer-url { position: absolute; left: 392px; top: 60px; font-size: 22px; font-weight: 700; letter-spacing: 3px; }
  .footer-url span { color: var(--teal-soft); }
</style>
</head>
<body>
<div class="sheet">
  <div class="abs hero-photo" role="img" aria-label="Photo of a young couple holding their baby at home"></div>

  <div class="abs brand"><span class="brand-dot"></span><span class="brand-name">Harbor Perks</span></div>

  <p class="abs eyebrow-lede">One small decision</p>
  <h1 class="abs headline">A lifetime of<br>protection</h1>
  <p class="abs subhead">Permanent life insurance + long-term care coverage,<br>starting at <b>$1 a day.</b></p>

  <h2 class="abs section-title" style="top:238px">CHOOSE YOUR DAILY INVESTMENT</h2>

  <div class="abs tier" style="left:87px">
    <div class="tier-price">$1<small>/ day</small></div>
    <svg class="tier-arrow" width="40" height="6" viewBox="0 0 40 6"><path d="M0 3h36M33 0l4 3-4 3" stroke="#1aafbf" stroke-width="1.4" fill="none"/></svg>
    <div class="tier-amount">$20,000</div><div class="tier-label">Life Insurance</div>
  </div>
  <div class="abs tier hero" style="left:305px">
    <div class="tier-price">$2<small>/ day</small></div>
    <svg class="tier-arrow" width="40" height="6" viewBox="0 0 40 6"><path d="M0 3h36M33 0l4 3-4 3" stroke="#0b4ea2" stroke-width="1.4" fill="none"/></svg>
    <div class="tier-amount">$40,000</div><div class="tier-label">Life Insurance</div>
  </div>
  <div class="abs tier" style="left:521px">
    <div class="tier-price">$3<small>/ day</small></div>
    <svg class="tier-arrow" width="40" height="6" viewBox="0 0 40 6"><path d="M0 3h36M33 0l4 3-4 3" stroke="#1aafbf" stroke-width="1.4" fill="none"/></svg>
    <div class="tier-amount">$60,000</div><div class="tier-label">Life Insurance</div>
  </div>
  <span class="abs tier-tag">Most Popular</span>
  <p class="abs tier-caption">Rate locked at enrollment. Benefit never decreases.</p>

  <h2 class="abs section-title" style="top:400px">THREE BENEFITS. ONE POLICY.</h2>
  <p class="abs section-sub" style="top:419px">Your money works three ways.</p>

  <div class="abs benefit" style="left:60px;width:208px">
    <div class="benefit-head">
      <span class="icon-disc"><svg width="20" height="18" viewBox="0 0 20 18"><path d="M2 16h16M4 14V9M8 14V6M12 14V8M16 14V3" stroke="#fff" stroke-width="2"/></svg></span>
      <span class="benefit-title">1. Cash Value<br>&nbsp;&nbsp;&nbsp;&nbsp;Growth</span>
    </div>
    <p class="benefit-body">Averages 6% annually over the last 50 years guaranteed never tofall below 3%. Better than any savings account. And if you ever need it, you can borrow against it. It's your money.</p>
  </div>
  <div class="abs col-rule" style="left:274px"></div>
  <div class="abs benefit" style="left:292px;width:218px">
    <div class="benefit-head">
      <span class="icon-disc"><svg width="18" height="18" viewBox="0 0 18 18"><path d="M3 14V8a6 6 0 0 1 12 0v6zM1 16h16" fill="#fff" stroke="#fff" stroke-width="1.5"/></svg></span>
      <span class="benefit-title">2. Tax-Free<br>&nbsp;&nbsp;&nbsp;&nbsp;Death Benefit</span>
    </div>
    <p class="benefit-body">From day one, your family is protected. The full benefit is paid tax-free to the person you choose — no waiting period, no exceptions. That's your legacy, preserved.</p>
  </div>
  <div class="abs col-rule" style="left:517px"></div>
  <div class="abs benefit" style="left:538px;width:222px">
    <div class="benefit-head">
      <span class="icon-disc"><svg width="20" height="18" viewBox="0 0 20 18"><path d="M10 15S3 10 3 6a3.5 3.5 0 0 1 7-1 3.5 3.5 0 0 1 7 1c0 4-7 9-7 9z" fill="#fff"/></svg></span>
      <span class="benefit-title">3. Long-Term<br>&nbsp;&nbsp;&nbsp;&nbsp;Care Coverage</span>
    </div>
    <p class="benefit-body">70% of Americans will need long-term care. This plan pays 75% of your benefit — upfront and tax-free — to cover those costs while you're still alive. Your retirement savings stay intact. Your family stays protected.</p>
  </div>

  <h2 class="abs work-title">ALREADY HAVE LIFE<br>INSURANCE THROUGH WORK?</h2>
  <p class="abs work-lede">That's term. It ends when you need it most.</p>
  <p class="abs work-body" style="top:645px">Term life insurance is designed for temporary needs — protecting your paycheck, your mortgage, your kids while they're home. When you retire, the house is paid off and your children are grown. Term ends because the need ends.</p>
  <p class="abs work-body" style="top:724px">But one need never ends: your final expenses and the cost of long-term care. This permanent plan stays with you after retirement — when term coverage is gone and getting new coverage is expensive or impossible.</p>

  <div class="abs compare">
    <div class="compare-head">TERM LIFE</div>
    <div class="compare-head">THIS PLAN</div>
    <ul class="compare-col term">
      <li>Gets more expensive with age</li>
      <li>Ends at retirement</li>
      <li>No cash value</li>
      <li>Temporary protection only</li>
    </ul>
    <ul class="compare-col plan">
      <li>Rate locked forever at enrollment</li>
      <li>Stays with you after retirement</li>
      <li>Builds real cash value</li>
      <li>Permanent protection for life</li>
    </ul>
  </div>

  <h2 class="abs section-title" style="top:803px">WHAT MAKES THIS DIFFERENT</h2>
  <p class="abs section-sub" style="top:821px">Built for you. Stays with you</p>

  <div class="abs feature" style="left:60px;width:135px">
    <svg class="feature-icon" width="34" height="34" viewBox="0 0 34 34"><circle cx="10" cy="6" r="4" fill="#1aafbf"/><circle cx="24" cy="6" r="4" fill="#1aafbf"/><path d="M5 12h10v10h-2v10H7V22H5zM19 12h10v10h-2v10h-6V22h-2z" fill="#1aafbf"/></svg>
    <div><p class="feature-title">Guaranteed<br>Issued</p><p class="feature-body">No medical exams. No questions asked. You qualify.</p></div>
  </div>
  <div class="abs feature-rule" style="left:200px"></div>
  <div class="abs feature" style="left:208px;width:135px">
    <svg class="feature-icon" width="30" height="30" viewBox="0 0 30 30"><path d="M15 0l2 4 4 .5-3 3 .8 4-3.8-2-3.8 2 .8-4-3-3 4-.5z" fill="#0c2577"/><circle cx="15" cy="17" r="4" fill="#0c2577"/><path d="M5 30c0-6 4-9 10-9s10 3 10 9z" fill="#0c2577"/></svg>
    <div><p class="feature-title teal">Group<br>Rate</p><p class="feature-body">Because you work here, you get pricing individuals can't access on their own.</p></div>
  </div>
  <div class="abs feature-rule" style="left:347px"></div>
  <div class="abs feature" style="left:356px;width:138px">
    <svg class="feature-icon" width="28" height="30" viewBox="0 0 28 30"><circle cx="12" cy="18" r="11" fill="#1aafbf"/><path d="M8 22l8-8" stroke="#fff" stroke-width="1.6"/><circle cx="8.5" cy="14.5" r="1.5" fill="#fff"/><circle cx="15.5" cy="21.5" r="1.5" fill="#fff"/><rect x="19" y="4" width="8" height="6" fill="#0c2577"/><path d="M20.5 4V2a2.5 2.5 0 0 1 5 0v2" stroke="#0c2577" stroke-width="1.4" fill="none"/></svg>
    <div><p class="feature-title">Rate Locked<br>Forever</p><p class="feature-body">Your premium never increases. Your benefit never decreases.</p></div>
  </div>
  <div class="abs feature-rule" style="left:497px"></div>
  <div class="abs feature" style="left:510px;width:132px">
    <svg class="feature-icon" width="28" height="24" viewBox="0 0 28 24"><rect x="1" y="6" width="26" height="17" rx="2" fill="#0c2577"/><path d="M9 6V2h10v4" stroke="#0c2577" stroke-width="2" fill="none"/><path d="M7 6v17M21 6v17" stroke="#fff" stroke-width="1"/></svg>
    <div><p class="feature-title teal">Portable</p><p class="feature-body">Change jobs. Retire. Your policy comes with you at the same rate.</p></div>
  </div>
  <div class="abs feature-rule" style="left:646px"></div>
  <div class="abs feature" style="left:660px;width:120px">
    <svg class="feature-icon" width="26" height="28" viewBox="0 0 26 28"><circle cx="8" cy="6" r="4" fill="#0c2577"/><circle cx="18" cy="8" r="3" fill="#1aafbf"/><path d="M1 20c0-6 3-9 7-9s7 3 7 9z" fill="#0c2577"/><circle cx="18" cy="20" r="6" fill="#1aafbf"/><path d="M15 20l2 2 4-4" stroke="#fff" stroke-width="1.6" fill="none"/></svg>
    <div><p class="feature-title">Family<br>Coverage</p><p class="feature-body">Protect your spouse and children under the same plan.</p></div>
  </div>

  <footer class="abs footer">
    <p class="tagline">Protect retirement.<br><span class="accent">Preserve dignity.</span><br>Plan ahead.</p>
    <div class="footer-rule"></div>
    <p class="footer-info">Be on the lookout for your personalized coverage details.<br>Brokered by Harbor Perks · Underwritten by TrueLedger</p>
    <p class="footer-url">www.<span>harborperks</span>.com</p>
  </footer>
</div>
</body>
</html>
```